Cold Pressed Juice Cleanse Brochure

We need to update our existing brochure (attached) with new photography. The wording can remain the same, however, on the CLEANSE ORDER page (panel 3), make these changes. You can also consult our website for additional design ideas. www.brightpeartonic.com.au

Upon waking, drink your first juice, and drink your next juice in order every two hours thereafter.

Harbour Reset. This is our most popular cleanse & perfect for those who want to balance great-tasting juices with high efficiency. This bundle includes:
1. Tidal Whirls
2. Ember Fizz or Ember rouge
3. Fern X
4. Red or Sunny Patch
5. Fern Q
6. Either Dream Blend

Summit Reset
Our most intense & lowest calorie cleanse - you get the maximum results in the minimum amount of time. This bundle includes:
1. Meadow Snap or Celery
2. Ember Fizz
3. Tidal Whirl
4. Fern Q
5. Fern X
6. Oaty Dream Blend

Hearth Reset
The organic Hearth Reset. We've curated a mixture of smoothies, cold-pressed juices, bone broth and nut mylks to keep you clean and warm through the winter months. The broth together with our Ember Fizz and Oaty Dream Blend can all be gently heated on the stove to nourish you from the inside and out. This bundle includes:
1. Tidal Whirl
2. Ember Fizz or Ember Rouge
3. Sunny Patch or Red
4. Organic Bone Broth
5. Fern Q
6. Either Dream Blend

We truly believe in our Cleanses and the results speak for themselves. NOURISH your body with antioxidant-rich juices. HELP your digestion and encourage a healthy balance of flora in your belly. ENJOY better overall well-being and weight loss.

Target Market(s)

25-60 year old M & F

Industry/Entity Type

Health And Wellness

Requirements
Must have
• The info on the existing brochure together with the new information listed in the project description.

```html
<!DOCTYPE html>
<html lang="en">
<head>
<meta charset="utf-8">
<title>Bright Pear Cleanse Brochure</title>
<link href="https://fonts.googleapis.com/css2?family=Kaushan+Script&family=Open+Sans:wght@400;600;700&display=swap" rel="stylesheet">
<style>
:root{
  --backdrop:#3b3b3b;
  --paper:#ffffff;
  --paper-soft:#f2f2ef;
  --green:#6aab3a;
  --green-dark:#2f5a24;
  --ink:#3a3a3a;
  --ink-soft:#666;
  --badge:#555;
}
*{margin:0;padding:0;box-sizing:border-box}
html,body{width:789px;height:1200px;overflow:hidden;background:var(--backdrop)}
body{position:relative;font-family:"Open Sans",Arial,sans-serif;color:var(--ink)}
.panel{position:absolute;background:var(--paper);overflow:hidden}
.photo{position:absolute}
.script{font-family:"Kaushan Script",cursive;color:var(--green);font-weight:400}
p,li{font-size:8.5px;line-height:1.45}
ol{list-style:none}
.bundle li{font-weight:700;font-size:8.5px;line-height:1.6}

/* cover */
.cover{left:0;top:0;width:394px;height:585px}
.cover .photo{left:0;top:0;width:394px;height:310px;background:linear-gradient(135deg,#f4f3f0 0%,#e6e3dd 55%,#d9d2c6 100%)}
.handle{position:absolute;left:14px;top:14px;display:flex;align-items:center;gap:6px;font-size:9px;font-weight:600;color:var(--ink)}
.handle i{width:12px;height:12px;background:var(--green);display:block}
.brand{position:absolute;left:0;width:394px;top:405px;text-align:center}
.brand .dot{width:42px;height:42px;border-radius:50%;background:var(--green);margin:0 auto 10px}
.brand span{font-size:30px;font-weight:700;color:var(--green);letter-spacing:.5px}
.site{position:absolute;left:0;width:394px;bottom:18px;text-align:center;font-size:10px;font-weight:600;color:var(--ink)}

/* tips */
.tips{left:395px;top:0;width:394px;height:585px;background:var(--paper-soft)}
.tips .photo{left:0;top:0;width:394px;height:165px;background:linear-gradient(90deg,#5f8d2e,#8fb84a 30%,#e2a23a 55%,#b9c85e 75%,#efe3cc)}
.tips h2{position:absolute;left:150px;top:176px;font-size:34px}
.tip-list{position:absolute;left:28px;top:236px;width:340px}
.tip-list li{display:flex;gap:10px;margin-bottom:14px}
.tip-list b{flex:none;width:18px;height:18px;background:var(--badge);color:#fff;font-size:9px;display:flex;align-items:center;justify-content:center}
.tips .note{position:absolute;left:28px;top:515px;width:340px;font-size:7.5px;color:var(--ink-soft);border-top:1px solid #ccc;padding-top:8px}

/* order */
.order{left:0;top:600px;width:394px;height:600px}
.order .photo.hero{left:0;top:0;width:394px;height:290px;background:linear-gradient(120deg,#fafaf8 0%,#eef1e8 40%,#6fa23a 60%,#b9d38a 80%,#f6f6f2 100%)}
.order .intro{position:absolute;left:16px;top:20px;width:150px}
.order .intro h2{font-size:28px;margin-bottom:6px}
.order .intro p{font-size:9px}
.swoosh{position:absolute;left:0;top:262px}
.classic{position:absolute;left:16px;top:320px;width:180px}
.classic h2{font-size:26px;margin-bottom:6px}
.classic p{margin-bottom:8px}
.order .photo.bottles{left:200px;top:380px;width:185px;height:200px;background:linear-gradient(90deg,#5f8d2e,#9cc053 25%,#e08a3c 45%,#d8502e 60%,#7aa33a 78%,#efe3cc)}

/* bundles */
.bundles{left:395px;top:600px;width:394px;height:600px;background:var(--paper-soft)}
.bundle-block{position:absolute;left:16px;width:205px}
.bundle-block h2{font-size:24px;margin-bottom:5px}
.bundle-block p{margin-bottom:7px}
.green-block{top:16px}
.broth-block{top:290px}
.bundles .photo{left:228px;width:155px;height:130px}
.bundles .ph-green{top:70px;background:linear-gradient(90deg,#4e7f27,#86b145 30%,#e6a33c 55%,#a9c55a 75%,#efe3cc)}
.bundles .ph-broth{top:345px;background:linear-gradient(90deg,#c8b58d,#d8573a 30%,#e6a33c 50%,#8fb84a 75%,#efe3cc)}
.rule{position:absolute;left:16px;right:16px;top:272px;height:1px;background:#cfcfcf}
.closing{position:absolute;left:16px;right:16px;bottom:16px;background:var(--green-dark);color:#fff;padding:10px 12px}
.closing p{font-size:8px;color:#fff}
</style>
</head>
<body>

<section class="panel cover">
  <div class="photo" role="img" aria-label="Bottle of nut milk beside a bowl of cashews on a pale stone surface"></div>
  <div class="handle"><i></i>@brightpeartonic</div>
  <div class="brand"><div class="dot"></div><span>bright pear</span></div>
  <div class="site">www.brightpeartonic.com.au</div>
</section>

<section class="panel tips">
  <div class="photo" role="img" aria-label="Row of cold pressed juice bottles in green, orange and cream"></div>
  <h2 class="script">Cleanse Tip</h2>
  <ol class="tip-list">
    <li><b>1</b><p>Start each day with a 250ml glass of warm lemon water to kick start early morning hydration, absorption and metabolism.</p></li>
    <li><b>2</b><p>Consume your juice at regular intervals throughout the day and finish each one.</p></li>
    <li><b>3</b><p>Shake before consuming and chew your juice like food to get the digestive enzymes working for you.</p></li>
    <li><b>4</b><p>Exercise does wonders for distracting from hunger and craving the food, but keep moving!</p></li>
    <li><b>5</b><p>Cleansing affects people differently with a variety of side effects that might arise including headaches, nausea, fatigue and irritability. Breathe deeply and relax. The fun shall pass!</p></li>
  </ol>
  <p class="note">No added sugar • No concentrates • No preservatives • Dairy free • Australian made &amp; owned • Cold Pressed from 100% whole fruits &amp; vegetables</p>
</section>

<section class="panel order">
  <div class="photo hero" role="img" aria-label="Green juice bottle surrounded by fresh leafy greens"></div>
  <div class="intro">
    <h2 class="script">Cleanse Order</h2>
    <p>Upon waking, drink your first juice, and drink your next juice in order every two hours thereafter.</p>
  </div>
  <svg class="swoosh" width="394" height="50" viewBox="0 0 394 50"><path d="M0 30 Q200 0 394 22 L394 50 L0 50 Z" fill="#fff"/><path d="M0 30 Q200 0 394 22" stroke="#6aab3a" stroke-width="4" fill="none"/></svg>
  <div class="classic">
    <h2 class="script">Harbour Reset</h2>
    <p>This is our most popular cleanse &amp; perfect for those who want to balance great-tasting juices with high efficiency. This bundle includes:</p>
    <ol class="bundle">
      <li>1. Tidal Whirls</li>
      <li>2. Ember Fizz or Ember rouge</li>
      <li>3. Fern X</li>
      <li>4. Red or Sunny Patch</li>
      <li>5. Fern Q</li>
      <li>6. Either Dream Blend</li>
    </ol>
  </div>
  <div class="photo bottles" role="img" aria-label="Six juice bottles from the Harbour Reset bundle"></div>
</section>

<section class="panel bundles">
  <div class="bundle-block green-block">
    <h2 class="script">Summit Reset</h2>
    <p>Our most intense &amp; lowest calorie cleanse - you get the maximum results in the minimum amount of time. This bundle includes:</p>
    <ol class="bundle">
      <li>1. Meadow Snap or Celery</li>
      <li>2. Ember Fizz</li>
      <li>3. Tidal Whirl</li>
      <li>4. Fern Q</li>
      <li>5. Fern X</li>
      <li>6. Oaty Dream Blend</li>
    </ol>
  </div>
  <div class="photo ph-green" role="img" aria-label="Six juice bottles from the Summit Reset bundle"></div>
  <div class="rule"></div>
  <div class="bundle-block broth-block">
    <h2 class="script">Hearth Reset</h2>
    <p>The organic Hearth Reset. We've curated a mixture of smoothies, cold-pressed juices, bone broth and nut mylks to keep you clean and warm through the winter months. The broth together with our Ember Fizz and Oaty Dream Blend can all be gently heated on the stove to nourish you from the inside and out. This bundle includes:</p>
    <ol class="bundle">
      <li>1. Tidal Whirl</li>
      <li>2. Ember Fizz or Ember Rouge</li>
      <li>3. Sunny Patch or Red</li>
      <li>4. Organic Bone Broth</li>
      <li>5. Fern Q</li>
      <li>6. Either Dream Blend</li>
    </ol>
  </div>
  <div class="photo ph-broth" role="img" aria-label="Six bottles from the Hearth Reset bundle including bone broth"></div>
  <div class="closing">
    <p>We truly believe in our Cleanses and the results speak for themselves. NOURISH your body with antioxidant-rich juices. HELP your digestion and encourage a healthy balance of flora in your belly. ENJOY better overall well-being and weight loss.</p>
  </div>
</section>

</body>
</html>
```